Rising Builders WA Pull Up Banner

Rising Builders Western Australia (‘RBWA’) exists to coordinate professional development and networking opportunities for the ~9,500 Young Engineer members of Technica Guild residing in the state of Western Australia. Further information and background on Technica Guild, Rising Builders Guild, and Rising Builders Western Australia can be found at:

https://www.technicaguild.example.org/about-us
http://www.technicaguild.example.org/rising-builders
http://www.technicaguild.example.org/rising-builders-western-australia

We require a design for a new pull-up banner, similar to all of those exemplified by http://lnkz.example/QWMPa .

The intended use of the banner is for display at Rising Builders WA events. It should be able to act a signpost for people to identify the event from a distance (e.g.: from distance in a large conference room), and appear welcoming. It should also be able to be used as a generic banner (e.g.: for placement behind a speaker at a conference), and so should not be situation-specific (e.g.: contain “event here” or similar, which would be out of place in the example given above). Events at which it will be seen include technical conferences, after-work drinks, quiz nights, sports days, balls, and others.
Updates

Reason: Hi All, I am very sorry but I am currently on site for work. I will be providing feedback to everybody this weekend. Sorry for the delay and I am extending the deadline to allow adequate feedback to everybody. Thanks and again sorry for the inconvenience. Trevor

Reason: Hi All, I will be consulting with my committee in the next couple of days and we will make a decision for the final poster design by monday. Thanks all so much for your designs! I will provide more feedback shortly.

Target Market(s)

Young Professional Engineers aged 18 to 35

Industry/Entity Type

Events

Requirements
Must have
• • Consider the intended use of the banner

• Comply in all ways to the specifications noted in the attached document “artwork specs 850_1000mm lite_1.pdf”.

• Consider incorporation of “Technica Guild corporate logo red”, namely:
o CMYK: (C:5, M:93, Y:97, K:1)
o RGB: (R:230, G:0, B:0)
o Pantone colour match is 485

• As we are alternately referred to as RBWA or RBGWA within the organisation, no reference to either acronym should be included in the design. ‘Rising Builders WA’ is acceptable if required.

• Consider incorporation of the RBWA logo, attached as two eps files “TG_RBWA_WA*.eps”, however this logo is not required. It is also not inviolate and designers can alter it if required.
Should not have
• typical man with clipboard and hardhat
fishbowls or similar

```html
<!DOCTYPE html>
<html lang="en">
<head>
<meta charset="utf-8">
<title>Rising Builders WA – Pull Up Banner</title>
<link rel="stylesheet" href="https://fonts.googleapis.com/css2?family=Roboto+Condensed:wght@400;700;800&display=swap">
<style>
  :root {
    --guild-red: #e60000;
    --deep-red: #c8101a;
    --charcoal: #2b2b2b;
    --slate: #6e6f71;
    --paper: #ffffff;
    --silver-light: #f4f4f4;
    --silver-mid: #d5d6d8;
    --silver-dark: #a9abae;
    --stage: #ebebeb;
    --suit-navy: #2a3550;
  }
  * { box-sizing: border-box; margin: 0; padding: 0; }
  html, body { width: 1200px; height: 818px; overflow: hidden; }
  body {
    background: var(--stage);
    font-family: "Roboto Condensed", "Arial Narrow", sans-serif;
  }
  .banner {
    position: absolute;
    left: 400px;
    top: 14px;
    width: 400px;
    height: 790px;
    overflow: hidden;
    background: linear-gradient(160deg, var(--silver-light) 0%, var(--silver-mid) 45%, var(--silver-light) 70%, var(--silver-dark) 100%);
    box-shadow: 0 2px 10px rgba(0,0,0,0.12);
  }
  .banner__hero {
    position: absolute;
    left: 45px;
    top: 196px;
    width: 290px;
    height: 498px;
    background: radial-gradient(ellipse at 50% 22%, #e8c3ad 0%, #d9ab92 16%, var(--suit-navy) 34%, #1f2840 70%, #3a3f4c 100%);
    border-radius: 46% 46% 10px 10px / 28% 28% 10px 10px;
    opacity: 0.9;
  }
  .tag {
    position: absolute;
    display: flex;
    align-items: center;
    justify-content: center;
    text-transform: uppercase;
    white-space: nowrap;
  }
  .tag--welcome {
    left: 22px; top: 52px; width: 343px; height: 87px;
    background: var(--paper);
    color: var(--deep-red);
    font-weight: 800;
    font-size: 76px;
    letter-spacing: 0.5px;
    transform: rotate(-1deg);
  }
  .tag--group {
    left: 36px; top: 148px; width: 303px; height: 49px;
    background: var(--paper);
    color: var(--deep-red);
    font-weight: 700;
    font-size: 29px;
  }
  .tag--lead {
    left: 4px; top: 570px; width: 289px; height: 47px;
    background: var(--slate);
    color: var(--paper);
    font-weight: 700;
    font-size: 29px;
  }
  .tag--cta {
    left: 62px; top: 617px; width: 338px; height: 51px;
    background: var(--guild-red);
    color: var(--paper);
    font-weight: 700;
    font-size: 29px;
  }
  .banner__footer {
    position: absolute;
    left: 0; bottom: 0;
    width: 400px; height: 96px;
    background: var(--charcoal);
    display: flex;
    align-items: center;
    justify-content: center;
    gap: 12px;
  }
  .brand__mark {
    width: 34px; height: 34px;
    background: var(--guild-red);
  }
  .brand__text { color: var(--paper); line-height: 1.15; }
  .brand__name {
    font-weight: 700;
    font-size: 18px;
    text-transform: uppercase;
    letter-spacing: 0.5px;
  }
  .brand__sub { font-weight: 400; font-size: 11px; }
</style>
</head>
<body>
  <main class="banner">
    <div class="banner__hero" role="img" aria-label="Photo of a smiling young professional in a navy suit reaching out for a handshake"></div>
    <div class="tag tag--welcome">Welcome</div>
    <div class="tag tag--group">Rising Builders WA</div>
    <div class="tag tag--lead">Look forward to</div>
    <div class="tag tag--cta">Advancing your career.</div>
    <footer class="banner__footer">
      <span class="brand__mark"></span>
      <div class="brand__text">
        <div class="brand__name">Technica Guild</div>
        <div class="brand__sub">Rising Builders Western Australia</div>
      </div>
    </footer>
  </main>
</body>
</html>
```